Design a Professional Business Card for Velmora Arcs

Design a business card for Velmora Arcs, we are a National Sport Court Company.

West Region Address: 4175 Quill Harbor Ln, Suite #215 Englewood, Colorado 80467
East Region Address: 3817 Tamsin Rd E, Bradenton, Florida 34583

Target Market(s)

High End Residential & Institutional Clients

Industry/Entity Type

Design & Construction

Contact Information for Business Card

Logo/Brand/Colors/ name, number (provided in comments)

Requirements
Must have
• Colors only provided in logo
Should not have
• Any other colors not in existing logo (attached)

```html
<!DOCTYPE html>
<html lang="en">
<head>
<meta charset="utf-8">
<title>Velmora Arcs – Business Card</title>
<link href="https://fonts.googleapis.com/css2?family=Barlow:wght@600;700;800&family=Barlow+Condensed:wght@400;600&family=PT+Sans&display=swap" rel="stylesheet">
<style>
  :root {
    --navy: #1e3764;
    --green: #12673a;
    --teal: #79c2b6;
    --white: #ffffff;
    --ink: #1b1b1b;
    --edge: #2a2a2a;
  }
  html, body {
    margin: 0;
    width: 1200px;
    height: 962px;
    overflow: hidden;
    background: var(--white);
  }
  .card {
    position: absolute;
    left: 231px;
    width: 501px;
    height: 301px;
    display: block;
  }
  .card--front { top: 122px; }
  .card--back { top: 480px; }
  .brand-name { font-family: "Barlow", sans-serif; font-weight: 800; letter-spacing: 3px; }
  .role { font-family: "PT Sans", sans-serif; }
  .person-name { font-family: "Barlow Condensed", sans-serif; font-weight: 400; }
  .contact-line { font-family: "Barlow", sans-serif; font-weight: 600; fill: var(--ink); }
  .address-line { font-family: "Barlow Condensed", sans-serif; font-weight: 600; fill: var(--ink); }
</style>
</head>
<body>

<!-- Front of card -->
<svg class="card card--front" viewBox="0 0 900 540" xmlns="http://www.w3.org/2000/svg" aria-label="Velmora Arcs business card, front">
  <rect class="card-bg" width="900" height="540" fill="var(--navy)"/>
  <polygon class="title-band" points="0,135 430,135 559,425 0,425" fill="var(--white)"/>
  <polygon class="chevron-fill" points="410,135 453,0 470,0 440,135" fill="var(--white)"/>
  <g class="chevron" fill="none" stroke-linejoin="miter" stroke-miterlimit="10">
    <polyline points="461,-5 438,135 617,545" stroke="var(--green)" stroke-width="16"/>
    <polyline points="478,-5 450,135 629,545" stroke="var(--white)" stroke-width="8"/>
    <polyline points="495,-5 462,135 641,545" stroke="var(--green)" stroke-width="14"/>
  </g>

  <g class="brand-lockup">
    <circle cx="81" cy="234" r="57" fill="var(--green)"/>
    <text class="brand-name" x="158" y="228" font-size="44" fill="var(--navy)">VELMORA</text>
    <text class="brand-name" x="158" y="278" font-size="44" fill="var(--navy)">ARCS</text>
  </g>
  <text class="role" x="282" y="327" font-size="29" text-anchor="middle" fill="var(--navy)">CEO &amp; Founder</text>

  <circle class="brand-badge" cx="763" cy="157" r="92" fill="var(--green)" stroke="var(--white)" stroke-width="3"/>
  <rect width="900" height="540" fill="none" stroke="var(--edge)" stroke-width="2"/>
</svg>

<!-- Back of card -->
<svg class="card card--back" viewBox="0 0 900 540" xmlns="http://www.w3.org/2000/svg" aria-label="Velmora Arcs business card, back">
  <rect class="card-bg" width="900" height="540" fill="var(--navy)"/>
  <polygon class="contact-panel" points="335,116 900,116 900,406 460,406" fill="var(--white)"/>
  <polygon class="chevron-fill" points="460,406 487,406 443,540 430,540" fill="var(--white)"/>
  <g class="chevron" fill="none" stroke-linejoin="miter" stroke-miterlimit="10">
    <polyline points="257,-5 437,406 398,545" stroke="var(--green)" stroke-width="14"/>
    <polyline points="271,-5 449,406 413,545" stroke="var(--white)" stroke-width="8"/>
    <polyline points="285,-5 461,406 427,545" stroke="var(--green)" stroke-width="14"/>
  </g>

  <text class="person-name" x="878" y="67" font-size="66" text-anchor="end" fill="var(--teal)">Dorian L. Whitfield, ASLA</text>
  <text class="role" x="509" y="102" font-size="25" fill="var(--white)">CEO &amp; Founder</text>

  <g class="contact-icons" fill="none" stroke="var(--navy)" stroke-width="1.6" stroke-linecap="round" stroke-linejoin="round">
    <circle cx="478" cy="154" r="15" fill="var(--teal)" stroke="none"/>
    <path d="M471,146 l4,-1 l3,5 l-3,2 q2,5 6,7 l2,-3 l5,3 l-1,4 q-10,1 -16,-17 z"/>
    <circle cx="478" cy="219" r="15" fill="var(--teal)" stroke="none"/>
    <rect x="469" y="213" width="18" height="12"/>
    <polyline points="469,213 478,220 487,213"/>
    <circle cx="478" cy="266" r="15" fill="var(--teal)" stroke="none"/>
    <circle cx="478" cy="266" r="9"/>
    <ellipse cx="478" cy="266" rx="4" ry="9"/>
    <line x1="469" y1="266" x2="487" y2="266"/>
    <circle cx="478" cy="314" r="15" fill="var(--teal)" stroke="none"/>
    <path d="M478,324 q-7,-8 -7,-13 a7,7 0 0 1 14,0 q0,5 -7,13 z"/>
    <circle cx="478" cy="311" r="2.5"/>
  </g>

  <g class="contact-details">
    <text class="contact-line" x="507" y="159" font-size="22">Direct: (303) 555-0147</text>
    <text class="contact-line" x="507" y="186" font-size="22">Main&#160; : 1-800-555-0193</text>
    <text class="contact-line" x="507" y="226" font-size="22">email: dorian@velmoraarcs.com</text>
    <text class="contact-line" x="507" y="274" font-size="22">web: www.velmoraarcs.com</text>
    <text class="address-line" x="507" y="320" font-size="19">West Region Address: 4175 Quill Harbor Ln,</text>
    <text class="address-line" x="507" y="343" font-size="19">Suite #215 Englewood, Colorado 80467</text>
    <text class="address-line" x="507" y="366" font-size="19">East Region Address: 3817 Tamsin Rd E,</text>
    <text class="address-line" x="507" y="389" font-size="19">Bradenton, Florida 34583</text>
  </g>

  <g class="brand-lockup">
    <circle cx="94" cy="320" r="45" fill="var(--green)" stroke="var(--white)" stroke-width="2"/>
    <text class="brand-name" x="150" y="314" font-size="34" fill="var(--white)">VELMORA</text>
    <text class="brand-name" x="150" y="352" font-size="34" fill="var(--white)">ARCS</text>
  </g>
  <rect width="900" height="540" fill="none" stroke="var(--edge)" stroke-width="2"/>
</svg>

</body>
</html>
```